Cool Landing page with email address sign up (mockups provided)

I need a landing page for a service that will send a weekly email to people who are looking for jobs in startups. On the landing page there is a call to action (submit button) to register their email address. The service is called VentureCrew and it is a side project to try to assist startup companies with hiring people.

I just want one single form field "Email".

The feeling I want to give people is one of adventure. Imagine the person is living in Gdansk Poland, they are a technical/IT expert and have dreams of making it big in a Startup in London. This is his big chance, this is going to allow him to do it! He's signing up to a big promise! It should be cool, professional, exciting.

A major influence should be:
http://brassteapotcorner.com/

There should also be a call to tweet in a cool way like on (http://www.withinfoundry.org/).

Look at this - taking a leap of faith, like this:
http://kitebloomapp.com/wp-content/uploads/2011/09/19.jpg

This is super with the colours - striking!:
http://pelvora.org/

Fly your kit higher!:
http://tobiasvrenn.com/

If necessary use sex to sell:
http://kitebloomapp.com/wp-content/uploads/2011/09/24.jpg

Some original art would work:
http://kitebloomapp.com/wp-content/uploads/2011/09/fx_ss_group1_sm_filtered_0000s_0007_Layer-14.jpg

This is effective for a call to action, I'm looking to you to act!:
http://kitebloomapp.com/wp-content/uploads/2011/09/weblance.jpg
Take inspiration from:
http://www.withinfoundry.org/
http://venturecrew.org/
http://quarrymint.com/

***N.B.: I would prefer original art background over a photo

Also:
http://pixelfolioroom.com/inspiration/a-showcase-of-landing-pages-designed-for-conversion
especially:
http://pixelfolioroom.com/wp-content/uploads/2011/09/01-landing.jpg
http://pixelfolioroom.com/wp-content/uploads/2011/09/04-landing.jpg
http://pixelfolioroom.com/wp-content/uploads/2011/10/texture21.jpg

I really like the colouring from Tinker Ledger:
http://board.quillmatic.com/

Reason: I'm going to be away for a few days so I won't have enough time to properly provide feedback.

The payment is now guaranteed. This project is a single page only.

I've added a few more example landing pages that I like.

I've now added the venturecrew logo image that should be used.

I've updated brief with more examples of what I'm looking for

Reason: I'm still progressing with candidate designs.

Target Market(s)

Technical people, english not being their native language. Ambitious to work in London/Dublin in a tech startup company. They want to receive a weekly emails with startup jobs in london or dublin.

Requirements
Must have
• Eyes must be drawn to the email registration form to get them to submit their email address. The background image or website theme should encourage their desires to work in the big city in exciting startup companies.

Should have a prompt to tweet (once pressed I'll do my own popup)

```html
<!DOCTYPE html>
<html lang="en">
<head>
<meta charset="utf-8">
<title>VentureCrew — Startup jobs weekly</title>
<link rel="stylesheet" href="https://fonts.googleapis.com/css2?family=Comfortaa:wght@600&family=Noto+Sans:wght@400&family=Ubuntu:wght@300;400&display=swap">
<style>
  :root {
    --sky-top: #5fd3f3;
    --sky-mid: #9ee6fa;
    --sky-bottom: #c9f2fd;
    --frame-dark: #4a4038;
    --cream: #ece8dd;
    --white: #ffffff;
    --ink: #2b2b2b;
    --logo-grey: #a9a9a9;
    --accent-orange: #f26a10;
    --tab-top: #ffa743;
    --tab-bottom: #f2820f;
    --tab-edge: #d96c08;
    --green-top: #a8d84a;
    --green-bottom: #6fac1a;
    --green-edge: #5d8f18;
    --footer-top: #a48a77;
    --footer-bottom: #7d6453;
    --footer-band: #5a4a3e;
    --footer-text: #2a2119;
    --photo-tone: #3a3533;
  }
  * { box-sizing: border-box; margin: 0; padding: 0; }
  html, body { width: 1200px; height: 779px; overflow: hidden; }
  body { position: relative; background: var(--white); font-family: "Ubuntu", sans-serif; }

  .site-header {
    position: absolute; left: 0; top: 0; width: 1200px; height: 146px;
    border-top: 4px solid var(--frame-dark);
    background: radial-gradient(ellipse 60% 120% at 50% 0%, var(--sky-bottom), var(--sky-mid) 45%, var(--sky-top) 100%);
  }
  .site-header::after {
    content: ""; position: absolute; left: 0; right: 0; bottom: 0; height: 4px;
    background: linear-gradient(var(--sky-mid), var(--white));
  }
  .brand {
    position: absolute; left: 37px; top: 51px; width: 376px; height: 95px;
    background: linear-gradient(var(--white) 70%, #eef9fc);
    border-radius: 14px 14px 0 0;
    display: flex; align-items: center; justify-content: center; gap: 10px;
  }
  .brand-name { font-family: "Ubuntu", sans-serif; font-weight: 400; font-size: 44px; color: var(--logo-grey); letter-spacing: -0.5px; }
  .brand-dot { width: 14px; height: 14px; border-radius: 50%; background: #a6d80f; }

  .main-nav { position: absolute; left: 537px; top: 103px; display: flex; gap: 2px; }
  .main-nav a {
    display: block; height: 40px; line-height: 40px; text-align: center;
    font-family: "Comfortaa", sans-serif; font-weight: 600; font-size: 19px; color: var(--white);
    text-decoration: none; border-radius: 6px 6px 0 0;
    background: linear-gradient(var(--tab-top), var(--tab-bottom));
    border: 1px solid var(--tab-edge); border-bottom: none;
  }
  .tab-details { width: 122px; } .tab-company { width: 139px; } .tab-media { width: 122px; } .tab-why { width: 177px; }

  .hero {
    position: absolute; left: 0; top: 146px; width: 1200px; height: 461px;
    background: linear-gradient(var(--cream) 0, var(--cream) 78%, var(--white) 100%);
  }
  .hero-pitch {
    position: absolute; left: 49px; top: 68px; width: 660px;
    font-weight: 300; font-size: 33px; line-height: 38px; color: var(--ink);
  }
  .hero-pitch em { font-style: normal; color: var(--accent-orange); }

  .signup {
    position: absolute; left: 48px; top: 198px; width: 561px; height: 67px;
    background: var(--white); border-radius: 34px;
    box-shadow: inset 0 1px 3px rgba(0,0,0,.25), 0 1px 0 rgba(255,255,255,.8);
  }
  .signup-field {
    position: absolute; left: 24px; top: 0; height: 67px; width: 390px; border: 0; background: transparent;
    font-family: "Noto Sans", sans-serif; font-size: 19px; color: var(--ink); outline: none;
  }
  .signup-field::placeholder { color: var(--ink); }
  .signup-submit {
    position: absolute; right: 0; top: 1px; width: 155px; height: 65px; border-radius: 33px;
    background: linear-gradient(var(--green-top), var(--green-bottom));
    border: 1px solid var(--green-edge);
    font-family: "Ubuntu", sans-serif; font-weight: 300; font-size: 27px; color: #1f2a0c; cursor: pointer;
  }

  .hero-figure {
    position: absolute; left: 660px; top: 30px; width: 425px; height: 357px;
    background: radial-gradient(ellipse at 55% 50%, var(--photo-tone) 0, rgba(58,53,51,.55) 45%, rgba(236,232,221,0) 72%);
  }

  .site-footer {
    position: absolute; left: 0; top: 607px; width: 1200px; height: 172px;
    background: linear-gradient(var(--footer-top), var(--footer-bottom));
    border-top: 20px solid var(--footer-band);
    border-bottom: 6px double #e9e1d6;
  }
  .footer-nav { position: absolute; left: 49px; top: 63px; display: flex; gap: 16px; font-family: "Noto Sans", sans-serif; font-size: 15px; color: var(--footer-text); }
  .footer-nav a { color: var(--footer-text); text-decoration: none; }
  .footer-nav .sep { letter-spacing: 1px; }
  .copyright { position: absolute; right: 102px; top: 63px; font-family: "Noto Sans", sans-serif; font-size: 15px; color: var(--footer-text); }
</style>
</head>
<body>
  <header class="site-header">
    <div class="brand"><span class="brand-name">venturecrew</span><span class="brand-dot"></span></div>
    <nav class="main-nav">
      <a class="tab-details" href="#">Details</a>
      <a class="tab-company" href="#">Company</a>
      <a class="tab-media" href="#">Media</a>
      <a class="tab-why" href="#">Why Startup</a>
    </nav>
  </header>

  <main class="hero">
    <p class="hero-pitch"><em>Sign up</em> now for a simple, free weekly email of the best startup jobs near you.</p>
    <form class="signup" action="#">
      <input class="signup-field" type="email" name="email" placeholder="Enter your email address">
      <button class="signup-submit" type="submit">Register</button>
    </form>
    <div class="hero-figure" role="img" aria-label="Photo of a businessman in a dark suit leaping forward mid-stride"></div>
  </main>

  <footer class="site-footer">
    <nav class="footer-nav">
      <a href="#">Details</a><span class="sep">::</span>
      <a href="#">Company</a><span class="sep">::</span>
      <a href="#">Media</a><span class="sep">::</span>
      <a href="#">Why Startup</a>
    </nav>
    <p class="copyright">© 2011, All Rights Reserved</p>
  </footer>
</body>
</html>
```